"Harborline Inc." Needs a Logo Design and Business Card

The name of the company is "Harborline Inc."
Our Business decription, which should appear on the front of the Business Card along with the logo and business name is:
"Boutique Global Procurement and Management Services"
We offer the following SERVICES that should be listed on the back of the Business Card :
"Consultants"
"Management"
"Business Research & Development"
"Sourcing Agent"
"Distributors"
We would like to see designs that use the colors
burnt orange and,
stainless steel
Business card designs should be innovatively modern and contemporary
Telephone number and email address should be on the back of the card
The name of the firm is "Harborline Inc.
Steel

```html
<!DOCTYPE html>
<html lang="en">
<head>
<meta charset="utf-8">
<title>Harborline Inc. — Business Card</title>
<link href="https://fonts.googleapis.com/css2?family=Dosis:wght@400;600&family=Didact+Gothic&display=swap" rel="stylesheet">
<style>
  :root {
    --burnt-orange: #f7941d;
    --steel: #8a8c8f;
    --steel-dark: #6d6f72;
    --backdrop: #8f9194;
    --paper: #ffffff;
  }
  html, body {
    margin: 0;
    padding: 0;
    width: 1200px;
    height: 1012px;
    overflow: hidden;
    background: var(--backdrop);
  }
  .stage {
    position: relative;
    width: 1200px;
    height: 1012px;
  }
  .card {
    position: absolute;
    left: 250px;
    width: 700px;
    height: 400px;
    box-sizing: border-box;
    box-shadow: 0 6px 18px rgba(0,0,0,0.25);
  }
  .card-front {
    top: 70px;
    background: var(--burnt-orange);
  }
  .card-back {
    top: 540px;
    background: var(--paper);
  }
  .frame {
    position: absolute;
    inset: 16px;
    border: 1.5px solid var(--paper);
  }
  .card-back .frame {
    inset: 18px;
    border: 2px solid var(--burnt-orange);
  }

  /* Front */
  .front-brand {
    position: absolute;
    left: 50%;
    top: 118px;
    transform: translateX(-50%);
    width: 300px;
    text-align: center;
    color: var(--paper);
    font-family: "Dosis", sans-serif;
  }
  .front-brand .brand-name {
    font-weight: 400;
    font-size: 40px;
    letter-spacing: 1px;
    line-height: 1;
    padding-bottom: 10px;
    border-bottom: 2px solid var(--paper);
  }
  .front-brand .brand-tagline {
    margin-top: 10px;
    font-weight: 600;
    font-size: 19px;
    line-height: 1.15;
  }

  /* Back */
  .back-brand {
    position: absolute;
    left: 44px;
    top: 40px;
    display: flex;
    align-items: center;
    color: var(--burnt-orange);
    font-family: "Dosis", sans-serif;
  }
  .back-brand .brand-name {
    font-weight: 400;
    font-size: 28px;
    padding-right: 12px;
    border-right: 2px solid var(--burnt-orange);
    line-height: 1.3;
  }
  .back-brand .brand-tagline {
    padding-left: 12px;
    font-size: 15px;
    line-height: 1.2;
  }
  .services {
    position: absolute;
    left: 52px;
    top: 140px;
    font-family: "Didact Gothic", sans-serif;
    font-size: 21px;
    color: var(--steel-dark);
    line-height: 1.3;
    white-space: nowrap;
  }
  .services .row { display: block; }
  .services .row-second { padding-left: 150px; }
  .services .dot {
    display: inline-block;
    width: 8px;
    height: 8px;
    border-radius: 50%;
    background: var(--steel);
    margin: 0 9px;
    vertical-align: middle;
  }
  .contact {
    position: absolute;
    left: 44px;
    top: 260px;
    font-family: "Dosis", sans-serif;
    font-size: 19px;
    color: var(--burnt-orange);
    line-height: 1.35;
  }
</style>
</head>
<body>
<main class="stage">
  <section class="card card-front" aria-label="Business card front">
    <div class="frame"></div>
    <div class="front-brand">
      <div class="brand-name">Harborline Inc.</div>
      <div class="brand-tagline">Worldwide Trade Procurement<br>and Service Partners</div>
    </div>
  </section>

  <section class="card card-back" aria-label="Business card back">
    <div class="frame"></div>
    <div class="back-brand">
      <div class="brand-name">Harborline Inc.</div>
      <div class="brand-tagline">Worldwide Trade Procurement<br>and Service Partners</div>
    </div>
    <div class="services">
      <span class="row">Consultant<span class="dot"></span>Managemen<span class="dot"></span>Business Research &amp; Development</span>
      <span class="row row-second">Sourcing Agent<span class="dot"></span>Distributor</span>
    </div>
    <div class="contact">
      <div class="phone">Cel. xx-xxx-xxx</div>
      <div class="email">Email. example@harborline.com</div>
    </div>
  </section>
</main>
</body>
</html>
```